Brochure/flyer for Tuftmoor Nappy Company

My Business name is Plover Wrenlyn Nappies
I am wanting a A4 size brochure (Flyer) to be folded twice. Measurements when folded 210 x 99 mm
I am just about to launch my Modern Cloth Nappy Products and i am wanting a brochure to target new mum's who aren't familiar with Modern cloth nappies and also for mums who are familiar with modern cloth nappies but are looking at trying my brand.
I want the Brochure to be very informative but yet Simple to read. I want people to feel like they want to buy my nappies after they read my Brochure.
The Brochure can be reworded and additional information can be added if you feel its needed, But i would like all the information listed below to be on the brochure.

MOTO: Cloth Nappies The Modern Way

The nappy design is designed in Australia and Australian Owned.

WHY USE CLOTH?
-Save thousands of Dollars
-Easy to use
-Looks Cute
-Super Absorbency
It costs approximately $3000 to use disposable nappies on a child from birth until 2 and a half years, that is Approximately 6000 nappies going into Landfill. This is based on a child going through 6-8 nappies per day.
Modern cloth nappies, on the other hand, cost around $500 for a full stash of 24 nappies. This allows for the child to wear 6-8 nappies per day with a load of nappies going in the wash every 2-3 days. As we have a range of nappies that are one-size-fits-most for bubs ranging from 3kg to 18kg, that $500 would cover your complete stash from birth right through to toilet training, Not to mention the money you would save by using the nappies again for any subsequent Children you may have.
Eliminates your baby's exposure to harmful Chemicals that can be in disposable nappies.
The manufacturing and use of disposable nappies can amount to 2-3 times more wasted water than using cloth nappies
Using Disposable Nappies fill up our landfill, Disposable nappies take more than 100 years to decompose, possibly up to 500 years.

PRODUCTS AVAILABLE:
Newborn: All in One (AIO) Fits approx 2-7kg
Velcro All in Two, One size Fits Most (OSFM) fits approx 3 to 18kg
Snap All in Two, One size Fits Most (OSFM) Fits Approx 3 to 18kg
Extra Inserts
Wetbags
Bamboo Biodegradable liners

The Materials used and features:
All in 2 Nappy (AI2):
Outer Shell Features- A waterproof TPU shell to keep all the wetness in.
Lining is a made of Microfleece material which is soft on baby's skin and Wicks moisture away from the baby's skin it is also very fast drying
Double leg Gussets to avoids any potential side leg Leaks
a poo guard at the back to reduce any leaks from occurring up the back
Insert is Made from 70% Bamboo and 30% Organic Cotton, The extra trim insert with extra absorbency qualities that can easily be double up for a heavy wetting baby or for an all night solution.

Insert snaps in and out Which is easy to remove and replace
A Pocket opening is also available to add a Booster in for long naps or for night time use. Insert is 2 layers sewn together and then folded twice to create 6 layers of absorbency. Unsnap insert from shell for washing, As there is not 3 layers sewn together like most inserts, it dries much quicker and washes more thoroughly, therefore less chance of smells accumulating

Why are these inserts so great?
– Super soft and silky
– Very breathable
– Naturally Anti-bacterial
– Absorbs 3 to 4 times more than cotton
– Doesn't feel sticky or uncomfortable when wet

The newborn nappy has a TPU waterproof Shell and is a all in one (AIO), has 4 layers of absorbency of 70% Bamboo and 30% Organic Cotton, With Microfleece lining which is super soft on newborns delicate skin.
The newborn nappy has a snap to hold down the front of the nappy where the umbilical cord will be for the first week or so. there is also snaps to adjust the size that little bit smaller for Premature babies or small babies. There is also double leg gussets to avoid any leaks around the legs. There is also a Poo guard at the back to avoid any leaks coming up from the back. The waist has a cross over snap for a extra small waist

PRICING:
One Size Fits Most:
Velcro: $25.95
Snap: $25.95
All In One Newborn:
$19.95

PACKAGES:
Price Depends on What nappies you choose for your package

Trial 3 pack: 5% Discount
6 Pack: 10% Discount
12 Pack: 15% Discount
24 Pack: 20% discount

Extra Inserts $7.00
Wetbags: $10
Bamboo Biodegradable Liners: $10
Contact Details:
Jolene Pridmore
Phone: 0491730284
E-mail: ploverwrenlynnappies@mailzenbox.com
Facebook: www.socialnookhub.com/PloverWrenlynNappies

I have changed a few things on the brief so please read carefully before changing or making another design,

Thanks :) 

Target Market(s)

Mums and Dads, care takers, Guardians and grandparents

Industry/Entity Type

Baby

Requirements
Must have
• Must have the Logo and picture i have sent but you are welcome to put other pictures of babies but please do not put pictures of babies with disposable nappies on. and if you are going to put pics of babies i would prefer the pictures not to show how the Velcro or snaps look at the front of the nappy. for example: put pictures that show the nappy side on or from the back. You could put pictures of babies or of nature etc "saving the Environment"
Should not have
• no pictures of other cloth nappy brands No disposable nappies

```html
<!DOCTYPE html>
<html lang="en">
<head>
<meta charset="utf-8">
<title>Plover Wrenlyn Nappies – Tri-fold Brochure</title>
<link href="https://fonts.googleapis.com/css2?family=Arvo:wght@400;700&display=swap" rel="stylesheet">
<style>
  :root {
    --magenta: #e5189b;
    --magenta-soft: #f7b3dd;
    --blush: #fde6f4;
    --yellow: #ffe44d;
    --ink: #1a1a1a;
    --white: #ffffff;
    --stage: #2a2a2a;
    --grey-light: #f4f4f4;
    --grey-mid: #a9a9a9;
    --lilac: #a86cc9;
  }
  * { box-sizing: border-box; margin: 0; padding: 0; }
  html, body { width: 1200px; height: 900px; overflow: hidden; }
  body {
    background: var(--stage);
    font-family: "Arvo", Georgia, serif;
    color: var(--ink);
    position: relative;
  }
  .spread {
    position: absolute;
    left: 300px;
    width: 600px;
    height: 424px;
    display: flex;
    background: var(--white);
    box-shadow: 0 4px 14px rgba(0,0,0,.45);
  }
  .spread--outside { top: 16px; }
  .spread--inside { top: 460px; }
  .panel {
    width: 200px;
    height: 100%;
    position: relative;
    overflow: hidden;
    font-size: 6px;
    line-height: 1.35;
  }
  .panel--magenta { background: var(--magenta); color: var(--white); }

  /* outside: pricing panel */
  .flower-strip {
    height: 62px;
    background: radial-gradient(circle at 25% 45%, var(--magenta-soft) 0 18px, transparent 19px),
                radial-gradient(circle at 85% 30%, var(--magenta) 0 12px, transparent 13px),
                linear-gradient(90deg, var(--blush), var(--white));
  }
  .pricing { padding: 8px 16px 0; }
  .pricing__title {
    color: var(--magenta);
    text-align: center;
    font-size: 10px;
    font-weight: 700;
    letter-spacing: .5px;
    margin-bottom: 4px;
  }
  .pricing__list { font-weight: 700; font-size: 6.3px; margin-bottom: 6px; }
  .pricing__list p { margin-bottom: 0; }
  .pricing__gap { height: 6px; }
  .photo-babies {
    position: absolute;
    left: 0; right: 0; bottom: 0;
    height: 92px;
    background: linear-gradient(180deg, #fbf3ee, #ecd2c3);
  }

  /* outside: contact panel */
  .panel--contact {
    background: linear-gradient(90deg, #cfcfcf 0%, var(--white) 35%, var(--white) 65%, #bdbdbd 100%);
  }
  .contact {
    position: absolute;
    left: 0; right: 0;
    top: 235px;
    text-align: center;
    padding: 0 18px;
  }
  .brand-mark {
    display: flex;
    align-items: center;
    justify-content: center;
    gap: 4px;
    font-size: 7px;
    color: var(--ink);
    margin-bottom: 8px;
  }
  .brand-mark__dot {
    width: 14px; height: 14px; border-radius: 50%;
    background: var(--lilac);
  }
  .contact__details { font-size: 5px; line-height: 1.5; }

  /* outside: cover panel */
  .cover-flowers {
    position: absolute;
    top: 0; right: 0;
    width: 120px; height: 80px;
    background: radial-gradient(circle at 70% 40%, var(--magenta-soft) 0 26px, transparent 27px),
                radial-gradient(circle at 25% 20%, #f26bbf 0 14px, transparent 15px);
    opacity: .85;
  }
  .cover-brand {
    position: absolute;
    left: 0; right: 0;
    top: 232px;
    display: flex;
    flex-direction: column;
    align-items: center;
    gap: 8px;
  }
  .cover-brand__dot {
    width: 30px; height: 30px; border-radius: 50%;
    background: var(--lilac);
  }
  .cover-brand__name {
    font-size: 15px;
    color: var(--yellow);
    text-align: center;
    line-height: 1.2;
  }

  /* inside: why cloth panel */
  .why { padding: 14px 14px 0; }
  .motto__title { font-size: 20px; color: var(--magenta); font-weight: 700; line-height: 1; }
  .motto__sub { font-size: 7px; color: var(--ink); margin: 2px 0 0 60px; }
  .why-block {
    display: flex;
    gap: 8px;
    margin: 10px 0 8px;
  }
  .why-block__flower {
    width: 26px; height: 26px; border-radius: 50%;
    background: radial-gradient(circle, #c9a2de, var(--lilac));
    flex: none;
    margin-top: 4px;
  }
  .why-block__title { font-size: 6.5px; font-weight: 700; margin-bottom: 2px; }
  .why-list { list-style: none; color: var(--magenta); font-size: 6px; }
  .why-list li::before {
    content: "";
    display: inline-block;
    width: 3px; height: 3px;
    background: var(--lilac);
    border-radius: 50%;
    margin-right: 3px;
    vertical-align: middle;
  }
  .body-copy p { margin-bottom: 5px; font-weight: 700; }
  .photo-baby-lying {
    position: absolute;
    left: 0; right: 0; bottom: 0;
    height: 92px;
    background: linear-gradient(160deg, #fff5ef, #efd6c6 60%, #f5ece6);
  }

  /* inside: features panel */
  .photo-sleeping {
    height: 92px;
    background: linear-gradient(120deg, #d9ebe8, #7fb1aa 55%, #c8dedb);
  }
  .features { padding: 8px 12px; }
  .features p { margin-bottom: 5px; }
  .heading-yellow { color: var(--yellow); font-weight: 700; font-size: 6.4px; }

  /* inside: products panel */
  .products { padding: 10px 12px 0; }
  .products p { margin-bottom: 5px; }
  .products__list p { margin-bottom: 0; }
  .products__list b { color: var(--yellow); }
  .inserts {
    position: absolute;
    left: 8px; right: 8px; bottom: 8px;
    background: var(--white);
    color: var(--ink);
    padding: 6px 8px;
    text-align: right;
  }
  .inserts__title { color: var(--magenta); font-weight: 700; font-size: 6.4px; margin-bottom: 2px; text-align: center; }
</style>
</head>
<body>

<section class="spread spread--outside" aria-label="Brochure outside">
  <div class="panel panel--pricing">
    <div class="flower-strip" role="img" aria-label="Pink flower decoration"></div>
    <div class="pricing">
      <h2 class="pricing__title">PRICING</h2>
      <div class="pricing__list">
        <p>One Size Fits Most:</p>
        <p>Velcro: $25.95</p>
        <p>Snap: $25.95</p>
        <div class="pricing__gap"></div>
        <p>All In One Newborn:</p>
        <p>$19.95</p>
      </div>
      <h2 class="pricing__title">PACKAGES:</h2>
      <div class="pricing__list">
        <p>Price Depends on What nappies you choose for your package</p>
        <div class="pricing__gap"></div>
        <p>Trial 3 pack: 5% Discount</p>
        <p>6 Pack: 10% Discount</p>
        <p>12 Pack: 15% Discount</p>
        <p>24 Pack: 20% discount</p>
        <div class="pricing__gap"></div>
        <p>Extra Inserts $7.00</p>
        <p>Wetbags: $10</p>
        <p>Bamboo Biodegradable Liners: $10</p>
      </div>
    </div>
    <div class="photo-babies" role="img" aria-label="Photo of four babies sitting in a row"></div>
  </div>

  <div class="panel panel--contact">
    <div class="contact">
      <div class="brand-mark">
        <span class="brand-mark__dot"></span>
        <span>Plover Wrenlyn Nappies</span>
      </div>
      <div class="contact__details">
        <p>Contact: Jolene Pridmore</p>
        <p>Phone: 0491730284</p>
        <p>ploverwrenlynnappies@mailzenbox.com</p>
        <p>www.socialnookhub.com/PloverWrenlynNappies</p>
      </div>
    </div>
  </div>

  <div class="panel panel--magenta panel--cover">
    <div class="cover-flowers" role="img" aria-label="Pink flower decoration"></div>
    <div class="cover-brand">
      <span class="cover-brand__dot"></span>
      <span class="cover-brand__name">Plover Wrenlyn Nappies</span>
    </div>
  </div>
</section>

<section class="spread spread--inside" aria-label="Brochure inside">
  <div class="panel panel--why">
    <div class="why">
      <div class="motto">
        <p class="motto__title">Cloth Nappies</p>
        <p class="motto__sub">the modern way</p>
      </div>
      <div class="why-block">
        <div class="why-block__flower" role="img" aria-label="Small flower decoration"></div>
        <div>
          <p class="why-block__title">WHY USE CLOTH?</p>
          <ul class="why-list">
            <li>Save thousands of Dollars</li>
            <li>Easy to use</li>
            <li>Looks Cute</li>
            <li>Super Absorbency</li>
          </ul>
        </div>
      </div>
      <div class="body-copy">
        <p>It costs approximately $3000 to use disposable nappies on a child from birth until 2 and a half years, that is Approximately 6000 nappies going into Landfill. This is based on a child going through 6-8 nappies per day.</p>
        <p>Modern cloth nappies, on the other hand, cost around $500 for a full stash of 24 nappies. This allows for the child to wear 6-8 nappies per day with a load of nappies going in the wash every 2-3 days. As we have a range of nappies that are one-size-fits-most for bubs ranging from 3kg to 18kg, that $500 would cover your complete stash from birth right through to toilet training. Not to mention the money you would save by using the nappies again for any subsequent Children you may have.</p>
      </div>
    </div>
    <div class="photo-baby-lying" role="img" aria-label="Photo of a baby lying on a soft blanket"></div>
  </div>

  <div class="panel panel--magenta panel--features">
    <div class="photo-sleeping" role="img" aria-label="Photo of a sleeping baby"></div>
    <div class="features">
      <p>Eliminates your baby's exposure to harmful Chemicals that can be in disposable nappies. The manufacturing and use of disposable nappies can amount to 2-3 times more wasted water than using cloth nappies.</p>
      <p>Using Disposable Nappies fill up our landfill. Disposable nappies take more than 100 years to decompose, possibly up to 500 years.</p>
      <p class="heading-yellow">The Materials used and Features<br>All in 2 Nappy (AI2):</p>
      <p>Outer Shell Features: A waterproof TPU shell to keep all the wetness in.</p>
      <p>Lining is a made of Microfleece material which is soft on baby's skin and Wicks moisture away from the baby's skin, it is also very fast drying.</p>
      <p>Double leg Gussets to avoid any potential side leg Leaks, a poo guard at the back to reduce any leaks from occurring up the back.</p>
      <p>Insert is Made from 70% Bamboo and 30% Organic Cotton. The extra trim insert with extra absorbency qualities can easily be doubled up for a heavy wetting baby or for an all night solution.</p>
    </div>
  </div>

  <div class="panel panel--magenta panel--products">
    <div class="products">
      <p>Insert snaps in and out Which is easy to remove and replace. A Pocket opening is also available to add a Booster in for long naps or for night time use. Insert is 2 layers sewn together and then folded twice to create 6 layers of absorbency. Unsnap insert from shell for washing; it dries much quicker and washes more thoroughly.</p>
      <p>The newborn nappy has a TPU waterproof Shell and is a all in one (AIO), has 4 layers of absorbency of 70% Bamboo and 30% Organic Cotton, With Microfleece lining which is super soft on newborns delicate skin.</p>
      <p>The newborn nappy has a snap to hold down the front where the umbilical cord will be for the first week or so, snaps to adjust the size for Premature or small babies, double leg gussets, a Poo guard at the back and a cross over snap for an extra small waist.</p>
      <p class="heading-yellow">Products Available:</p>
      <div class="products__list">
        <p><b>Newborn:</b> All in One (AIO) Fits approx 2-7kg</p>
        <p><b>Velcro All in Two,</b> One size Fits Most (OSFM) fits approx 3 to 18kg</p>
        <p><b>Snap All in Two,</b> One size Fits Most (OSFM) Fits Approx 3 to 18kg</p>
        <p>Extra Inserts</p>
        <p>Wetbags</p>
        <p>Bamboo Biodegradable liners</p>
      </div>
    </div>
    <div class="inserts">
      <p class="inserts__title">Why are these inserts so great?</p>
      <p>Super soft and silky</p>
      <p>Very breathable</p>
      <p>Naturally Anti-bacterial</p>
      <p>Absorbs 3 to 4 times more than cotton</p>
      <p>Doesn't feel sticky or uncomfortable when wet</p>
    </div>
  </div>
</section>

</body>
</html>
```